Kaede Roasters

Full Shopify site .
About page

Merch page
Tshirts, hats, mugs

Coffee page
-sections
Single origin
Tomoe series
Sensu series
Decaf

KaedeX page
Cold brew
Coffee liquor
Absinthe Coffee

```html
<!DOCTYPE html>
<html lang="en">
<head>
<meta charset="utf-8">
<title>Kaede Roasters — Where Coffee Meets Art</title>
<link rel="stylesheet" href="https://fonts.googleapis.com/css2?family=Montserrat:wght@400;500;600;700;800;900&display=swap">
<style>
:root{
  --red:#e0333c;
  --red-deep:#c8232d;
  --ink:#1c1c1f;
  --text:#444348;
  --muted:#6e6d72;
  --white:#ffffff;
  --blush:#fdeef1;
  --blush-2:#f8d6de;
  --pink:#f1a9bb;
  --rose:#e57d9a;
  --navy:#2a2c4a;
  --line:#ececef;
  --grey:#f2f2f4;
}
*{box-sizing:border-box;margin:0;padding:0}
html,body{width:1200px;height:2592px;overflow:hidden}
body{font-family:"Montserrat",Arial,sans-serif;color:var(--text);background:var(--white)}

/* Header */
.site-header{height:64px;display:flex;align-items:center;justify-content:space-between;padding:0 48px;background:var(--white);border-bottom:1px solid var(--line)}
.brand{display:flex;align-items:center;gap:10px;font-weight:800;font-size:20px;color:var(--ink);letter-spacing:.5px}
.brand-dot{width:30px;height:30px;border-radius:50%;background:var(--red)}
.main-nav{display:flex;align-items:center;gap:30px;font-size:13px;font-weight:700;color:var(--ink);letter-spacing:.6px}
.nav-cta{background:var(--red);color:var(--white);padding:9px 18px;border-radius:4px}

/* Hero */
.hero{position:relative;height:626px;overflow:hidden}
.hero-art{position:absolute;inset:0;background:
  radial-gradient(ellipse at 85% 30%,#f6c7d6 0%,rgba(246,199,214,0) 45%),
  linear-gradient(180deg,#f3a3bc 0%,#e98aa8 45%,#c96a93 70%,#4b3a5e 100%)}
.hero-sun{position:absolute;left:170px;top:110px;width:390px;height:390px;border-radius:50%;background:var(--red);display:flex;align-items:center;justify-content:center}
.hero-title{font-size:66px;line-height:1.02;font-weight:900;color:var(--white);text-align:center;letter-spacing:1px}
.hero-copy{position:absolute;left:560px;top:420px;width:520px;text-align:center;color:var(--white);font-size:24px;font-weight:600;line-height:1.3}
.hero-copy strong{font-weight:800}
.hero-button{position:absolute;left:620px;top:530px;background:var(--navy);color:var(--white);font-weight:700;font-size:15px;letter-spacing:.6px;padding:15px 28px;border-radius:4px}

/* Shared section heading */
.section-head{text-align:center}
.section-mark{width:56px;height:56px;border-radius:50%;background:var(--red);margin:0 auto 16px}
.eyebrow{display:flex;align-items:center;justify-content:center;gap:12px;color:var(--red);font-weight:800;font-size:16px;letter-spacing:2px}
.eyebrow::before,.eyebrow::after{content:"";width:36px;height:2px;background:var(--red)}
.section-title{font-size:50px;font-weight:900;color:var(--ink);letter-spacing:1px;line-height:1.05;margin-top:4px}

/* Collections */
.collections{height:550px;padding-top:56px;background:linear-gradient(180deg,var(--blush) 0%,#fff 60%,#fff 100%)}
.collection-grid{display:flex;justify-content:center;gap:24px;margin-top:36px}
.collection-card{width:206px;height:272px;background:var(--white);border:1px solid var(--line);box-shadow:0 6px 18px rgba(0,0,0,.07)}
.collection-image{height:140px}
.img-origin{background:linear-gradient(135deg,#f6efe3,#d9b98a 60%,#b5432f)}
.img-tomoe{background:linear-gradient(135deg,#f3f0e8,#cfd8c0 55%,#9a8e6a)}
.img-sensu{background:linear-gradient(135deg,#fafafa,#d6d6d6 60%,#8c8c8c)}
.img-kaedex{background:linear-gradient(135deg,#f7e1e6,#e3a9b6 55%,#5a3a3a)}
.card-body{padding:12px 14px}
.card-title{font-size:15px;font-weight:800;color:var(--ink)}
.card-text{font-size:11px;line-height:1.45;color:var(--muted);margin-top:5px}
.card-link{display:inline-block;margin-top:8px;font-size:11px;font-weight:700;color:var(--red)}

/* Merch */
.merch{height:800px;padding-top:96px;background:var(--white)}
.merch-grid{display:flex;justify-content:center;gap:40px;margin-top:48px}
.merch-card{width:240px;text-align:center}
.merch-image{height:264px;border:1px solid var(--line);box-shadow:0 6px 18px rgba(0,0,0,.08)}
.img-tee{background:linear-gradient(160deg,#f4f4f6,#dcdce0 70%,#f0b6c5)}
.img-hat{background:linear-gradient(160deg,#e9e9ec,#3a3a3e 55%,#141416)}
.img-mug{background:linear-gradient(160deg,#f6f6f7,#e4e4e8 60%,#e9a9b8)}
.merch-title{font-size:16px;font-weight:800;color:var(--ink);margin-top:18px}
.merch-text{font-size:12px;line-height:1.45;color:var(--muted);margin:6px 14px 0}
.merch-link{display:inline-block;margin-top:10px;font-size:12px;font-weight:700;color:var(--red)}

/* Story */
.story{height:460px;display:flex}
.story-art{width:560px;background:
  radial-gradient(circle at 60% 40%,#f6c7d6 0%,rgba(246,199,214,0) 35%),
  linear-gradient(160deg,#ef4a4f 0%,var(--red-deep) 70%,#a81c25 100%)}
.story-content{flex:1;background:linear-gradient(90deg,var(--blush) 0%,#fff8f9 100%);padding:60px 90px 0 60px}
.story-content .section-mark{margin:0 0 14px 0}
.story-content .eyebrow{justify-content:flex-start}
.story-content .eyebrow::after{display:none}
.story-content .section-title{font-size:48px}
.story-sub{font-size:18px;font-weight:800;color:var(--red);margin-top:4px}
.story-text{font-size:12px;line-height:1.55;color:var(--text);margin-top:10px;max-width:440px}
.story-button{display:inline-block;margin-top:18px;background:var(--red);color:var(--white);font-weight:700;font-size:12px;letter-spacing:.6px;padding:10px 18px;border-radius:4px}

/* Footer */
.site-footer{height:92px;display:flex;align-items:center;justify-content:center;background:var(--white);font-size:12px;color:var(--muted);border-top:1px solid var(--line)}
</style>
</head>
<body>
<header class="site-header">
  <div class="brand"><span class="brand-dot"></span>Kaede Roasters</div>
  <nav class="main-nav">
    <span>HOME</span><span>ABOUT</span><span>COFFEE</span><span>KAEDEX</span><span>MERCH</span><span class="nav-cta">CONTACT</span>
  </nav>
</header>

<section class="hero">
  <div class="hero-art" role="img" aria-label="Illustration of a figure sitting on a hillside beneath a blossoming tree against a pink sunset sky"></div>
  <div class="hero-sun"><h1 class="hero-title">WHERE<br>COFFEE<br>MEETS<br>ART</h1></div>
  <p class="hero-copy">Experience the harmony of Japanese <strong>tradition</strong> and specialty <strong>coffee culture</strong></p>
  <span class="hero-button">DISCOVER OUR COFFEES</span>
</section>

<section class="collections">
  <div class="section-head">
    <div class="section-mark"></div>
    <div class="eyebrow">OUR</div>
    <h2 class="section-title">COLLECTIONS</h2>
  </div>
  <div class="collection-grid">
    <article class="collection-card">
      <div class="collection-image img-origin" role="img" aria-label="Drawing of coffee cherries and leaves"></div>
      <div class="card-body">
        <h3 class="card-title">Single Origin</h3>
        <p class="card-text">Explore traceable beans from distinct regions, roasted to reveal their unique terroir.</p>
        <span class="card-link">Learn More →</span>
      </div>
    </article>
    <article class="collection-card">
      <div class="collection-image img-tomoe" role="img" aria-label="Drawing of a coffee branch with flowers"></div>
      <div class="card-body">
        <h3 class="card-title">Tomoe Series</h3>
        <p class="card-text">Delicate floral and refined varieties, the rarest lots roasted gently at their peak.</p>
        <span class="card-link">Learn More →</span>
      </div>
    </article>
    <article class="collection-card">
      <div class="collection-image img-sensu" role="img" aria-label="Line drawing of a coffee plant"></div>
      <div class="card-body">
        <h3 class="card-title">Sensu Series</h3>
        <p class="card-text">Our signature blends, bold and adventurous, inspired by the spirit of the wandering traveler.</p>
        <span class="card-link">Learn More →</span>
      </div>
    </article>
    <article class="collection-card">
      <div class="collection-image img-kaedex" role="img" aria-label="Bottles of cold brew and coffee spirits"></div>
      <div class="card-body">
        <h3 class="card-title">KaedeX</h3>
        <p class="card-text">A limited series of cold brews and coffee spirits, flavored fusions for the adventurous palate.</p>
        <span class="card-link">Explore KaedeX →</span>
      </div>
    </article>
  </div>
</section>

<section class="merch">
  <div class="section-head">
    <div class="section-mark"></div>
    <div class="eyebrow">MERCH</div>
    <h2 class="section-title">&amp; LIFESTYLE</h2>
  </div>
  <div class="merch-grid">
    <article class="merch-card">
      <div class="merch-image img-tee" role="img" aria-label="White t-shirt with a blossom tree print"></div>
      <h3 class="merch-title">T-Shirts</h3>
      <p class="merch-text">Soft, stylish tees featuring our iconic blossom artwork. Wear your love for coffee.</p>
      <span class="merch-link">View T-Shirts →</span>
    </article>
    <article class="merch-card">
      <div class="merch-image img-hat" role="img" aria-label="Black cap with an embroidered emblem"></div>
      <h3 class="merch-title">Hats</h3>
      <p class="merch-text">Complete your look with our embroidered caps, subtle yet statement-making.</p>
      <span class="merch-link">Shop Hats →</span>
    </article>
    <article class="merch-card">
      <div class="merch-image img-mug" role="img" aria-label="White mug with printed artwork"></div>
      <h3 class="merch-title">Mugs</h3>
      <p class="merch-text">Enjoy your brew in beautiful mugs adorned with our signature design.</p>
      <span class="merch-link">Shop Mugs →</span>
    </article>
  </div>
</section>

<section class="story">
  <div class="story-art" role="img" aria-label="Illustration of a dark blossoming tree against a red background"></div>
  <div class="story-content">
    <div class="section-mark"></div>
    <div class="eyebrow">OUR</div>
    <h2 class="section-title">STORY</h2>
    <p class="story-sub">The Art of Roasting</p>
    <p class="story-text">Kaede Roasters was born from a passion for craftsmanship and culture. Inspired by the fleeting beauty of cherry blossoms, we honour the delicate balance between precision and artistry in every roast. From our humble beginnings to our ongoing journey, we invite you to share in our story and savour the flavours crafted with care.</p>
    <span class="story-button">READ MORE</span>
  </div>
</section>

<footer class="site-footer">© 2025 Kaede Roasters. Crafted with passion in Maplewood.</footer>
</body>
</html>
```